Flyer Design for Private Car Service

Flyer should cater to Business Travelers and Executives who travel Business Class or First Class.
Flyer should include images attached.
Flyer should include the below text
Dallas to Austin
Chauffeured SUVs
• Travel Dallas to Austin in a new 2025 Marlow Strider for $499 one-way
• Trip includes a Uniformed Chauffeur who has a Commercial Drivers License (CDL)
• You can Schedule Chauffeur Pickup at Your Home in Dallas
• Our Chauffeur will Drop You Off at Your Final Destination in Austin
• You can Schedule Chauffeur Return Pickup in Austin and Return Back to Dallas.
• We offer Faster Times on Door-to-Door Travel than Bluecrest Airways
• We offer Comparable Prices on Door-to-Door Travel Times than Bluecrest Airways
• All of our trips are insured with $500k of commercial auto insurance
• Our Passengers can Talk on Cell Phone & Conduct Quill calls Throughout Travel
• Our Passengers have Maximum Privacy, Comfort and First-Class Amenities.
• Our Passengers Avoid Harwick Vale Field and KPR Airport hassles & delays
• Member Brenton Chamber of Commerce, Larkmoor Chamber of Commerce.
• Book your trip today at www.ridemarquel.example
Target Market(s)
Business Travelers
Look and feel
Each slider illustrates characteristics of the customer's brand and the style your logo design should communicate.

```html
<!DOCTYPE html>
<html lang="en">
<head>
<meta charset="utf-8">
<title>Dallas to Austin Chauffeured SUVs</title>
<link rel="stylesheet" href="https://fonts.googleapis.com/css2?family=Roboto:ital,wght@0,400;0,700;0,900;1,700&display=swap">
<style>
  :root {
    --page: #b9b9b9;
    --ink: #0a0a0a;
    --white: #ffffff;
    --red: #e3232b;
    --photo-dark: #2b2a2c;
    --photo-light: #a7a39d;
  }
  html, body { margin: 0; padding: 0; width: 1200px; height: 1200px; overflow: hidden; background: var(--page); }
  .flyer {
    position: absolute; left: 212px; top: 51px; width: 776px; height: 1098px;
    background: radial-gradient(ellipse 340px 420px at 660px 820px, #3a3a3a 0%, #1b1b1b 45%, var(--ink) 75%), var(--ink);
    overflow: hidden; font-family: "Roboto", sans-serif; color: var(--white);
  }
  .shapes { position: absolute; left: 0; top: 0; }
  .brand {
    position: absolute; left: 436px; width: 340px; top: 192px; text-align: center;
    font-size: 30px; font-weight: 400; letter-spacing: 2px; color: var(--white);
  }
  .headline { position: absolute; right: 45px; top: 306px; text-align: right; font-weight: 700; line-height: 1; }
  .headline .line { display: block; font-size: 35px; margin-bottom: 6px; }
  .headline .big { display: block; font-size: 70px; font-weight: 900; color: var(--ink); margin-top: 0; }
  .offer { position: absolute; left: 44px; top: 426px; font-size: 22px; line-height: 1.25; }
  .offer em { font-weight: 700; }
  .offer .price { color: var(--red); font-size: 47px; font-weight: 900; vertical-align: -6px; }
  .features { position: absolute; left: 44px; top: 593px; margin: 0; padding: 0; list-style: none; font-size: 15.6px; line-height: 26px; }
  .features li::before { content: "> "; color: var(--red); font-weight: 700; }
  .features.secondary { top: 864px; }
  .cta { position: absolute; left: 0; width: 776px; top: 995px; text-align: center; font-size: 21px; }
  .cta strong { font-weight: 700; font-style: italic; }
  .url-row { position: absolute; left: 0; top: 1028px; width: 776px; height: 26px; }
  .url-row .rule { position: absolute; top: 11px; height: 5px; background: var(--red); }
  .url-row .rule.left { left: 0; width: 244px; }
  .url-row .rule.right { left: 566px; width: 210px; }
  .url { position: absolute; left: 244px; width: 322px; text-align: center; top: 0; font-size: 19px; letter-spacing: 3px; color: var(--red); }
</style>
</head>
<body>
<main class="flyer">
  <svg class="shapes" width="776" height="1098" viewBox="0 0 776 1098">
    <defs>
      <linearGradient id="photoTone" x1="0" y1="0" x2="1" y2="1">
        <stop offset="0" stop-color="var(--photo-light)"/>
        <stop offset="0.5" stop-color="var(--photo-dark)"/>
        <stop offset="1" stop-color="#6e6a66"/>
      </linearGradient>
    </defs>
    <polygon role="img" aria-label="Photo: uniformed chauffeur assisting a business traveler with luggage beside a black SUV" points="0,0 514,0 391,381 0,381" fill="url(#photoTone)"/>
    <polygon class="title-panel" points="431,260 776,260 776,509 346,509" fill="var(--red)"/>
  </svg>

  <div class="brand">Marquel Rides</div>

  <h1 class="headline" style="margin:0">
    <span class="line">Dallas to Austin</span>
    <span class="line">Chauffeured</span>
    <span class="big">SUVs</span>
  </h1>

  <p class="offer" style="margin:0">
    Travel Dallas to Austin<br>
    in a new <em>2025 Marlow Strider</em><br>
    for <span class="price">$499</span> one-way
  </p>

  <ul class="features">
    <li>Trip includes a Uniformed Chauffeur who has a Commercial Drivers License (CDL)</li>
    <li>You can Schedule Chauffeur Pickup at Your Home in Dallas</li>
    <li>Our Chauffeur will Drop You Off at Your Final Destination in Austin</li>
    <li>You can Schedule Chauffeur Return Pickup in Austin and Return Back to Dallas.</li>
    <li>We offer Faster Times on Door-to-Door Travel than Bluecrest Airways</li>
    <li>We offer Comparable Prices on Door-to-Door Travel Times than Bluecrest Airways</li>
    <li>All of our trips are insured with $500k of commercial auto insurance</li>
    <li>Our Passengers can Talk on Cell Phone &amp; Conduct Quill calls Throughout Travel</li>
    <li>Our Passengers have Maximum Privacy, Comfort and First-Class Amenities.</li>
  </ul>

  <ul class="features secondary">
    <li>Our Passengers Avoid Harwick Vale Field and KPR Airport hassles &amp; delays</li>
    <li>Member Brenton Chamber of Commerce, Larkmoor Chamber of Commerce.</li>
  </ul>

  <p class="cta" style="margin:0"><strong>Book your trip today</strong> at</p>
  <div class="url-row">
    <span class="rule left"></span>
    <span class="url">www.ridemarquel.example</span>
    <span class="rule right"></span>
  </div>
</main>
</body>
</html>
```